BRC Business cards

We are a medium sized property company based in London and require a logo, Business card which reflects a professional company and incorporates our catchy name.

Our statement is (Building for the future) we like colours such as royal blue, greens and light browns but will look at anything.

Contact Information for Business Card

Brookcrest Estates Limited
Unit 4, 15-17 Farrowby Lane
London
SE22 7QN

Web: www.brookcrestestates-example.com

Email: brookcrestltd@mailbox-example.com

Telephone: +44-208-555-0142
Fax: +44-208-555-0187

```html
<!DOCTYPE html>
<html lang="en">
<head>
<meta charset="utf-8">
<title>Brookcrest Estates Limited – Business Card</title>
<link rel="stylesheet" href="https://fonts.googleapis.com/css2?family=Oswald:wght@700&family=Arimo:wght@400&display=swap">
<style>
  :root {
    --page-bg: #e9e6e1;
    --card-white: #ffffff;
    --royal-blue: #2c3d96;
    --deep-blue: #1f2c78;
    --sky-blue: #5a74c4;
    --leaf-green: #1f9a3c;
    --sun-yellow: #f2e21a;
    --ink-white: #ffffff;
  }
  * { box-sizing: border-box; margin: 0; padding: 0; }
  html, body {
    width: 900px;
    height: 1200px;
    overflow: hidden;
    background: var(--page-bg);
  }
  .business-card {
    position: absolute;
    left: 120px;
    top: 50px;
    width: 660px;
    height: 1100px;
    background: var(--card-white);
    overflow: hidden;
    box-shadow: 0 4px 18px rgba(0,0,0,0.18);
  }
  .brand-mark {
    position: absolute;
    left: 50%;
    top: 80px;
    width: 170px;
    height: 170px;
    margin-left: -85px;
    border-radius: 50%;
    background: var(--royal-blue);
  }
  .brand-name {
    position: absolute;
    left: 0;
    right: 0;
    top: 315px;
    text-align: center;
    font-family: "Oswald", "Arial Narrow", sans-serif;
    font-weight: 700;
    color: var(--royal-blue);
    line-height: 1;
  }
  .brand-name .primary {
    display: block;
    font-size: 96px;
    letter-spacing: 1px;
  }
  .brand-name .secondary {
    display: block;
    margin-top: 12px;
    font-size: 50px;
    letter-spacing: 2px;
  }
  .swoosh {
    position: absolute;
    left: 0;
    top: 0;
    width: 660px;
    height: 1100px;
  }
  .skyline-area {
    position: absolute;
    left: 0;
    right: 0;
    bottom: 0;
    height: 400px;
    background: linear-gradient(to bottom, rgba(90,116,196,0) 0%, rgba(90,116,196,0.45) 55%, rgba(31,44,120,0.75) 100%);
  }
  .contact-details {
    position: absolute;
    left: 20px;
    right: 20px;
    top: 715px;
    text-align: center;
    font-family: "Arimo", Arial, sans-serif;
    font-size: 27px;
    color: var(--ink-white);
    line-height: 1.55;
  }
  .contact-details .group + .group { margin-top: 32px; }
  .contact-details p { white-space: nowrap; }
</style>
</head>
<body>
  <div class="business-card">
    <div class="brand-mark"></div>
    <div class="brand-name">
      <span class="primary">BROOKCREST</span>
      <span class="secondary">ESTATES LIMITED</span>
    </div>

    <svg class="swoosh" viewBox="0 0 660 1100" aria-hidden="true">
      <path d="M0,565 C180,515 420,605 660,515 L660,1100 L0,1100 Z" fill="var(--leaf-green)"/>
      <path d="M0,625 C220,565 440,635 660,545 L660,1100 L0,1100 Z" fill="var(--sun-yellow)"/>
      <path d="M0,665 C220,605 450,665 660,585 L660,1100 L0,1100 Z" fill="var(--royal-blue)"/>
    </svg>

    <div class="skyline-area" role="img" aria-label="Faint city skyline of office towers across the lower blue panel"></div>

    <div class="contact-details">
      <div class="group">
        <p>Unit 4, 15-17 Farrowby Lane</p>
        <p>London SE22 7QN</p>
      </div>
      <div class="group">
        <p>Telephone: +44-208-555-0142</p>
        <p>Fax: +44-208-555-0187</p>
      </div>
      <div class="group">
        <p>Web: www.brookcrestestates-example.com</p>
        <p>Email: brookcrestltd@mailbox-example.com</p>
      </div>
    </div>
  </div>
</body>
</html>
```